Property Developer Business Card design

We need a business card design including a logo that will be used to create a brand for us. We are property developers and just starting out so we are small and not looking to be huge. We want to add value to existing property owners by way of developing their property. Typically this property would be the family home. We would like to see colors of Maroon and Cream with Maroon being the major color in the scheme. We note that the Chromyx Shade System colors are:
1815 Maroon CVC and 715 Cream CVC or in the computer color spectrum, the colors are as listed below.
Color Spectrum
Maroon Cream
0 127 24 255
236 1 240 191
60 2 163 91
Finally our tagline is the following (without the quote marks of course) "Building Value in Family Homes Today"

Industry/Entity Type

Computer

Contact Information for Business Card

Beth M Rowland, Director
0472 615 804
Tivmor Holdings (Qld) Pty Ltd
PO Box 561, TANSLEY VALE BC Q 4097

Font styles to use
Other font styles liked:
• Century Gothic

Requirements
Must have
• The color scheme and our tagline.
The Chromyx Shade System colors are:
Color Spectrum
Maroon Cream
0 127 24 255
236 1 240 191
60 2 163 91
Nice to have
• In the attached example of a business card, we quite like the design. There are 4 of us in the partnership so there should be 4 building blocks and not 3. The font is wrong, we rather like Century Gothic for clarity and ease of reading. Please replace the royal blue color with our Maroon color and replace the white and green color with our Cream color. Perhaps some of the white writing might look better left in, so please play with that idea. It is not a strong idea of ours, just a "perhaps". We like the swirl underneath the block of buildings. We like the little blocks of light that appear strewn across the bottom right hand corner and in other places. We like the added curve in deep color at the bottom going towards a lighter version towards the top of the card. We like the layout of the example of the text of one of our Directors but not the font.

```html
<!DOCTYPE html>
<html lang="en">
<head>
<meta charset="utf-8">
<title>Tivmor Holdings – Business Card</title>
<link rel="stylesheet" href="https://fonts.googleapis.com/css2?family=Exo+2:wght@400;600&display=swap">
<style>
  :root {
    --maroon: #c8202f;
    --maroon-deep: #9e1420;
    --cream: #f2d79a;
    --cream-soft: #f7e6bd;
    --gold-text: #c9a961;
    --ink: #2b2b2b;
    --charcoal: #343434;
    --paper: #ffffff;
    --paper-shade: #eeeeee;
    --stage: #e4e2de;
  }
  * { box-sizing: border-box; margin: 0; padding: 0; }
  html, body { width: 1057px; height: 1200px; overflow: hidden; }
  body {
    background: var(--stage);
    font-family: "Exo 2", "Century Gothic", sans-serif;
    position: relative;
  }
  .card {
    position: absolute;
    top: 207px;
    width: 450px;
    height: 786px;
    box-shadow: 0 6px 18px rgba(0,0,0,0.18);
    overflow: hidden;
  }
  .card--front {
    left: 50px;
    background: linear-gradient(160deg, var(--paper) 0%, var(--paper) 55%, var(--paper-shade) 100%);
  }
  .card--back {
    left: 557px;
    background: var(--charcoal);
  }

  /* front: brand */
  .brand {
    position: absolute;
    left: 36px;
    top: 44px;
    display: flex;
    align-items: center;
    gap: 10px;
  }
  .brand__mark {
    width: 34px;
    height: 34px;
    background: var(--maroon);
    flex: none;
  }
  .brand__name {
    color: var(--maroon);
    font-size: 17px;
    font-weight: 600;
    letter-spacing: 0.5px;
    white-space: nowrap;
  }
  .brand__tagline {
    position: absolute;
    left: 80px;
    top: 82px;
    color: var(--gold-text);
    font-size: 9px;
    letter-spacing: 1px;
    white-space: nowrap;
  }

  /* front: side bar */
  .side-bar {
    position: absolute;
    right: 28px;
    width: 22px;
  }
  .side-bar--maroon {
    top: 0;
    height: 330px;
    background: linear-gradient(to bottom, var(--maroon-deep), var(--maroon));
  }
  .side-bar--cream {
    top: 330px;
    height: 200px;
    background: var(--cream);
  }

  /* front: contact */
  .contact {
    position: absolute;
    right: 64px;
    top: 288px;
    text-align: right;
    color: var(--ink);
  }
  .contact__name {
    color: var(--maroon);
    font-size: 25px;
    font-weight: 600;
    letter-spacing: 1px;
    text-transform: uppercase;
    white-space: nowrap;
  }
  .contact__title {
    font-size: 12px;
    letter-spacing: 1.2px;
    text-transform: uppercase;
    margin-top: 2px;
  }
  .contact__line {
    font-size: 14px;
    letter-spacing: 0.8px;
    margin-top: 20px;
    white-space: nowrap;
  }
  .contact__line + .contact__line { margin-top: 16px; }
  .contact__address {
    font-size: 18px;
    letter-spacing: 0.6px;
    line-height: 1.45;
    margin-top: 30px;
    white-space: nowrap;
  }

  /* back */
  .back-brand {
    position: absolute;
    left: 0;
    right: 0;
    top: 330px;
    text-align: center;
  }
  .back-brand__mark {
    width: 58px;
    height: 58px;
    background: var(--maroon);
    margin: 0 auto 16px;
  }
  .back-brand__name {
    color: var(--maroon);
    font-size: 21px;
    font-weight: 600;
    letter-spacing: 1.5px;
    white-space: nowrap;
  }
  .back-brand__tagline {
    color: var(--cream-soft);
    font-size: 11px;
    letter-spacing: 1.5px;
    margin-top: 6px;
    white-space: nowrap;
  }
</style>
</head>
<body>
  <section class="card card--front" aria-label="Business card front">
    <div class="brand">
      <span class="brand__mark"></span>
      <span class="brand__name">Tivmor Holdings (Qld) Pty Ltd</span>
    </div>
    <p class="brand__tagline">Building Value in Family Homes Today</p>

    <div class="side-bar side-bar--maroon"></div>
    <div class="side-bar side-bar--cream"></div>

    <div class="contact">
      <p class="contact__name">Beth M Rowland</p>
      <p class="contact__title">General Manager</p>
      <p class="contact__line">0472 615 804</p>
      <p class="contact__line">0472 615 804</p>
      <p class="contact__line">beth@tivmorholdings.com.au</p>
      <p class="contact__line">www.tivmorholdings.com.au</p>
      <p class="contact__address">PO Box 561,<br>TANSLEY VALE BC Q 4097</p>
    </div>
  </section>

  <section class="card card--back" aria-label="Business card back">
    <div class="back-brand">
      <div class="back-brand__mark"></div>
      <p class="back-brand__name">Tivmor Holdings (Qld) Pty Ltd</p>
      <p class="back-brand__tagline">Building Value in Family Homes Today</p>
    </div>
  </section>
</body>
</html>
```